Bright Fern Property Services

Design a billboard with our logo that includes bullet points for
Property Maintenance, Plumbing, and Electrical, licensed and insured.
Phone number 865 471 3908

also add the website brightfernps-example.com

```html
<!DOCTYPE html>
<html lang="en">
<head>
<meta charset="utf-8">
<title>Bright Fern Property Services – Billboard</title>
<link href="https://fonts.googleapis.com/css2?family=Montserrat:wght@500;700;800&display=swap" rel="stylesheet">
<style>
  :root {
    --green: #3a9c35;
    --green-dark: #2d7f2a;
    --ink: #1e1e1e;
    --white: #ffffff;
    --paper: #f1f1f0;
    --backdrop: #e4e7eb;
    --sky: #7fa6cf;
    --foliage: #4f7d3a;
  }
  * { box-sizing: border-box; margin: 0; padding: 0; }
  html, body {
    width: 1200px; height: 970px; overflow: hidden;
    background: var(--backdrop);
    font-family: "Montserrat", Arial, sans-serif;
  }
  .billboard {
    position: absolute; left: 40px; top: 275px;
    width: 1120px; height: 420px;
    background: linear-gradient(180deg, var(--white), var(--paper));
    box-shadow: 0 8px 24px rgba(0,0,0,.18);
    overflow: hidden;
  }
  .billboard-shapes { position: absolute; inset: 0; }
  .brand {
    position: absolute; left: 750px; top: 46px; width: 350px;
    color: var(--green); font-weight: 700; text-align: center;
  }
  .brand-name { font-size: 44px; line-height: 1; letter-spacing: 1px; white-space: nowrap; }
  .brand-sub { font-size: 16px; letter-spacing: 3px; margin-top: 12px; color: var(--ink); white-space: nowrap; }
  .brand-rule {
    width: 300px; height: 2px; background: var(--green);
    margin: 12px auto 0;
  }
  .tagline {
    position: absolute; left: 640px; top: 206px; width: 460px;
    color: var(--white); font-weight: 800; font-size: 30px;
    line-height: 1.12; text-transform: uppercase; text-align: center;
    white-space: nowrap;
  }
  .web-pill {
    position: absolute; left: 670px; top: 314px; width: 420px; height: 46px;
    background: var(--ink); border-radius: 23px;
    color: var(--white); font-weight: 500; font-size: 19px; letter-spacing: 1px;
    white-space: nowrap;
    display: flex; align-items: center; justify-content: center;
    box-shadow: inset 0 2px 3px rgba(255,255,255,.2);
  }
  .phone {
    position: absolute; left: 670px; top: 370px; width: 420px;
    display: flex; align-items: center; justify-content: center; gap: 8px;
    color: var(--green-dark); font-weight: 800; font-size: 22px; letter-spacing: 1px;
    white-space: nowrap;
  }
  .phone-icon { width: 20px; height: 20px; }
  .services {
    position: absolute; left: 40px; top: 262px;
    display: flex; gap: 12px; list-style: none;
  }
  .service-card {
    width: 132px; height: 132px;
    background: linear-gradient(180deg, var(--white), var(--paper));
    border: 2px solid var(--green); border-radius: 6px;
    box-shadow: 0 3px 6px rgba(0,0,0,.25);
    display: flex; flex-direction: column; align-items: center; justify-content: center;
    gap: 6px; text-align: center;
  }
  .service-icon { width: 46px; height: 46px; }
  .service-label {
    font-weight: 700; font-size: 14px; line-height: 1.05;
    color: var(--ink); text-transform: uppercase;
  }
</style>
</head>
<body>
  <main class="billboard">
    <svg class="billboard-shapes" width="1120" height="420" viewBox="0 0 1120 420">
      <defs>
        <linearGradient id="photoTone" x1="0" y1="0" x2="0" y2="1">
          <stop offset="0" stop-color="var(--sky)"/>
          <stop offset="0.55" stop-color="#b9c9d6"/>
          <stop offset="1" stop-color="var(--foliage)"/>
        </linearGradient>
      </defs>
      <path class="green-band" d="M0 246 H470 C540 246 560 186 620 186 H1120 V300 H600 V372 H0 Z" fill="var(--green)"/>
      <path class="photo-border" d="M0 250 H480 C560 250 600 210 640 130 L710 0 H730 L660 134 C618 218 570 262 480 262 H0 Z" fill="var(--ink)"/>
      <path class="photo-area" role="img" aria-label="Photo of a white two-gabled house with grey siding, a patio and tall green trees under a blue sky"
            d="M0 0 H710 L640 130 C600 210 560 250 480 250 H0 Z" fill="url(#photoTone)"/>
    </svg>

    <div class="brand">
      <div class="brand-name">BRIGHT FERN</div>
      <div class="brand-sub">PROPERTY SERVICES LLC</div>
      <div class="brand-rule"></div>
    </div>

    <div class="tagline">Dependable property<br>care for peace of mind</div>
    <div class="web-pill">www.brightfernps-example.com</div>
    <div class="phone">
      <svg class="phone-icon" viewBox="0 0 24 24">
        <path d="M6.6 10.8a15.1 15.1 0 0 0 6.6 6.6l2.2-2.2a1 1 0 0 1 1-.25 11.4 11.4 0 0 0 3.6.57 1 1 0 0 1 1 1V20a1 1 0 0 1-1 1A17 17 0 0 1 3 4a1 1 0 0 1 1-1h3.5a1 1 0 0 1 1 1c0 1.25.2 2.45.57 3.57a1 1 0 0 1-.25 1z" fill="var(--green-dark)"/>
      </svg>
      <span>865 471 3908</span>
    </div>

    <ul class="services">
      <li class="service-card">
        <svg class="service-icon" viewBox="0 0 48 48">
          <path d="M6 24 L24 8 L42 24 H37 V42 H11 V24 Z" fill="var(--green)"/>
          <circle cx="33" cy="34" r="8" fill="var(--white)" stroke="var(--green)" stroke-width="3"/>
          <path d="M30 34 H36 M33 31 V37" stroke="var(--green)" stroke-width="2.5"/>
        </svg>
        <span class="service-label">Property<br>Maintenance</span>
      </li>
      <li class="service-card">
        <svg class="service-icon" viewBox="0 0 48 48">
          <path d="M10 8 H22 V28 H34 V40 H18 C13 40 10 37 10 32 Z" fill="var(--green)"/>
          <rect x="7" y="5" width="18" height="5" rx="1" fill="var(--green-dark)"/>
          <rect x="33" y="25" width="5" height="18" rx="1" fill="var(--green-dark)"/>
        </svg>
        <span class="service-label">Plumbing</span>
      </li>
      <li class="service-card">
        <svg class="service-icon" viewBox="0 0 48 48">
          <path d="M4 24 L24 6 L44 24 H39 V44 H9 V24 Z" fill="var(--green)"/>
          <path d="M26 18 L18 31 H24 L21 40 L30 26 H24 Z" fill="var(--white)"/>
        </svg>
        <span class="service-label">Electrical</span>
      </li>
      <li class="service-card">
        <svg class="service-icon" viewBox="0 0 48 48">
          <path d="M24 4 L38 9 V22 C38 32 31 38 24 41 C17 38 10 32 10 22 V9 Z" fill="var(--green)"/>
          <path d="M17 22 L22 27 L31 17" stroke="var(--white)" stroke-width="3.5" fill="none" stroke-linecap="round" stroke-linejoin="round"/>
        </svg>
        <span class="service-label">Licensed and<br>insured</span>
      </li>
    </ul>
  </main>
</body>
</html>
```